Corinne Bracket tutoring Advertising package - flyers, posters, business card and logo

I am looking for a flyer design for my tutoring business, it needs to explain what tutoring services I offer, how much I charge, why my services are worthwhile, it should include some photos of me and the tutoring centre,

It needs to include my phone number and my website. It should quote from some of the testimonials I have received from parents and children.

My website is www.corinnebracket-example.com My Facebook page can be found at https://www.facebook.com/corinnebrackettutoring These pages include a range of photos and quotes that you can use.

I am not sure about the colours and designs that I would like, that's why I'm using Sketchmarket!
I'm looking to appeal to parents inform them of my skills and experience.

I'm charging $45 for sessions of an hour and 15 minutes. 2 sessions per week will cost $80. I tutor Monday to Friday afternoons and evenings along with all day Saturdays. The assessment is free.

I tutor children from K-9 in English and Maths. I'm mainly aiming at parents whose children are struggling a little bit at school although I can help children who are doing well too.
I am highly skilled at helping children who can't read, I have a comprehensive program, the Pemberly program, that specifically teaches children the skills they need to read fluently and successfully.

Similarly I have had a lot of experience at helping children improve their Maths skills. I am well resourced with a wide range of hands on resources, paper resources and electronic resources.

Children will get better GRESTO results if I tutor them (GRESTO is the national series of tests in Australia).

I'm after a DL double sided flyer, and an A4 flyer. I'm also looking for two A2 posters and two A3 posters. Finally, I want a business card too. I don't have a logo for the business and I'd love to have one!

Target Market(s)

Parents of school aged children

Industry/Entity Type

Education

Colors

Designer to choose colors to be used in the design.

Requirements
Must have
• my name, my photo, length and cost of my sessions, email and phone contact details. Subjects and age ranges that I teach, times that I tutor. Website and/or Facebook page references. Quotes from Testimonials
Nice to have
• The A2 and A3 posters should complement each other.

```html
<!DOCTYPE html>
<html lang="en">
<head>
<meta charset="utf-8">
<title>Corinne Bracket Tutoring – A4 Flyer</title>
<link href="https://fonts.googleapis.com/css2?family=Lato:ital,wght@0,400;0,700;0,900;1,400&display=swap" rel="stylesheet">
<style>
  :root {
    --page-bg: #e6e6e6;
    --paper: #ffffff;
    --red: #d3141c;
    --red-deep: #8f0b10;
    --red-dark: #6e070b;
    --ink: #2b2b2b;
    --band: #1e1e1e;
    --band-light: #3a3a3a;
    --ring: #1c1c1c;
    --white: #ffffff;
  }
  * { box-sizing: border-box; margin: 0; padding: 0; }
  html, body {
    width: 1200px; height: 848px; overflow: hidden;
    background: var(--page-bg);
    font-family: "Lato", Arial, sans-serif;
  }
  .canvas {
    width: 1200px; height: 848px;
    display: flex; justify-content: center; align-items: center;
  }
  .flyer {
    position: relative;
    width: 600px; height: 848px;
    background: var(--paper);
    overflow: hidden;
    box-shadow: 0 0 14px rgba(0,0,0,.18);
  }
  .header-shape { position: absolute; left: 0; top: 0; width: 600px; height: 280px; }
  .headline {
    position: absolute; left: 50px; right: 40px; top: 34px;
    color: var(--white); text-align: center;
    font-weight: 700; font-size: 20px; line-height: 1.32;
    letter-spacing: .2px;
  }
  .photo-circle {
    position: absolute; border-radius: 50%;
    border: 7px solid var(--ring);
    box-shadow: 0 0 0 2px var(--red), 0 4px 10px rgba(0,0,0,.3);
  }
  .photo-circle--main {
    left: 48px; top: 150px; width: 240px; height: 240px;
    background: radial-gradient(circle at 40% 40%, #c99a5a, #8a5a2a 55%, #4a3526);
  }
  .photo-circle--room {
    left: 412px; top: 244px; width: 164px; height: 164px;
    background: radial-gradient(circle at 50% 55%, #b06a35, #7d5a3d 60%, #3f4656);
  }
  .photo-circle--shelf {
    left: 300px; top: 328px; width: 112px; height: 112px;
    background: radial-gradient(circle at 50% 45%, #cfc6b4, #8b8270 60%, #4b4640);
  }
  .details {
    position: absolute; left: 36px; top: 452px; width: 380px;
    color: var(--ink); font-size: 11px; line-height: 1.42;
  }
  .details p + p { margin-top: 7px; }
  .tutor-card { position: absolute; left: 430px; top: 468px; width: 150px; }
  .tutor-photo {
    width: 150px; height: 160px; border-radius: 14px;
    border: 4px solid var(--red);
    background: linear-gradient(160deg, #d9d4c6 0%, #b9b0a0 35%, #7fae62 75%, #6c9a52 100%);
  }
  .tutor-name {
    margin-top: -4px; margin-left: -8px; width: 166px;
    background: var(--band); color: var(--white);
    border-top: 3px solid var(--red);
    font-weight: 700; font-size: 12px; letter-spacing: 1px;
    text-transform: uppercase; text-align: center;
    padding: 6px 0;
  }
  .testimonials {
    position: absolute; left: 0; bottom: 0; width: 600px; height: 118px;
    background: linear-gradient(180deg, var(--band-light), var(--band) 60%);
    border-top: 4px solid var(--red);
    color: var(--white); padding: 10px 30px 0 30px;
    font-size: 8.6px; line-height: 1.38;
  }
  .testimonials::before {
    content: ""; position: absolute; left: 0; right: 0; top: -10px; height: 3px;
    background: var(--red-dark);
  }
  .testimonials h2 { font-size: 12px; font-weight: 900; margin-bottom: 3px; }
  .quote + .quote { margin-top: 4px; }
  .quote-author { display: block; font-weight: 700; }
</style>
</head>
<body>
<div class="canvas">
  <article class="flyer">
    <svg class="header-shape" viewBox="0 0 600 280" aria-hidden="true">
      <defs>
        <linearGradient id="headerRed" x1="0" y1="0" x2="1" y2="1">
          <stop offset="0" stop-color="#e41b23"/>
          <stop offset="1" stop-color="#9a0c12"/>
        </linearGradient>
      </defs>
      <path d="M0 0 H600 V270 Q380 200 0 215 Z" fill="var(--red-dark)"/>
      <path d="M0 0 H600 V250 Q360 170 0 195 Z" fill="url(#headerRed)"/>
      <path d="M0 0 H260 Q120 80 0 150 Z" fill="var(--red-deep)" opacity=".45"/>
    </svg>

    <h1 class="headline">I tutor children from K-9 in English and Maths. I'm mainly aiming at parents whose children are struggling a little bit at school although I can help children who are doing well too.</h1>

    <div class="photo-circle photo-circle--main" role="img" aria-label="Photo of the tutoring centre bookshelves"></div>
    <div class="photo-circle photo-circle--room" role="img" aria-label="Photo of the tutoring room with a study table"></div>
    <div class="photo-circle photo-circle--shelf" role="img" aria-label="Photo of a bookshelf corner in the centre"></div>

    <section class="details">
      <p>I'm charging $45 for sessions of an hour and 15 minutes. 2 sessions per week will cost $80. I tutor Monday to Friday afternoons and evenings along with all day Saturdays. The assessment is free.</p>
      <p>I am highly skilled at helping children who can't read, I have a comprehensive program, the Pemberly program, that specifically teaches children the skills they need to read fluently and successfully.</p>
      <p>Similarly I have had a lot of experience at helping children improve their Maths skills. I am well resourced with a wide range of hands on resources, paper resources and electronic resources.</p>
      <p>Children will get better GRESTO results if I tutor them (GRESTO is the national series of tests in Australia).</p>
    </section>

    <div class="tutor-card">
      <div class="tutor-photo" role="img" aria-label="Portrait photo of Corinne Bracket in front of bookshelves"></div>
      <div class="tutor-name">Corinne Bracket</div>
    </div>

    <section class="testimonials">
      <h2>Testimonials:</h2>
      <p class="quote">Our son has been tutored by Corinne now for the past 2 years - we have noticed a big improvement with his spelling and mathematics. This has also helped our son's confidence in his daily schooling and he now has started to enjoy school again. Thanks Corinne
        <span class="quote-author">Marcus and Helen Tarrow</span></p>
      <p class="quote">Our children love going to Corinne's!! Yes you read that right - they LOVE going to learn! Corinne has the ability to tap into each child's strengths and weaknesses and makes learning fun! Our children's grades have improved more so, our son just got awarded a distinction in a science competition! Thanks so much Corinne.
        <span class="quote-author">Priya Dellmont</span></p>
    </section>
  </article>
</div>
</body>
</html>
```